Attorney business card for two offices

Looking for a new business card design that can list both of my offices, one in Houston and one in West Texas. Want something masculine, easy to read, and conservative yet somewhat modern. Our current card has used a nautical star on it for years, but I am not necessarily attached to that. Also, a lot of our forms use dark green and orange. Second office address is P.O. Box 518, Marathon, Texas 79617

```html
<!DOCTYPE html>
<html lang="en">
<head>
<meta charset="utf-8">
<title>The Whitaker Law Firm – Business Card</title>
<link rel="stylesheet" href="https://fonts.googleapis.com/css2?family=Libre+Franklin:wght@400;500;700&display=swap">
<style>
  :root {
    --backdrop: #d4d4d4;
    --card: #ffffff;
    --green: #3b654b;
    --orange: #f7a81e;
    --name-white: #ffffff;
  }
  * { margin: 0; padding: 0; box-sizing: border-box; }
  html, body {
    width: 1200px; height: 795px; overflow: hidden;
    background: var(--backdrop);
    font-family: "Libre Franklin", Arial, sans-serif;
  }
  .business-card {
    position: absolute; left: 60px; top: 85px;
    width: 1080px; height: 625px;
    background: var(--card);
    overflow: hidden;
  }
  .name-panel {
    position: absolute; left: 0; top: 0;
    width: 415px; height: 100%;
    background: var(--green);
  }
  .accent-band {
    position: absolute; left: 415px; top: 0;
    width: 47px; height: 100%;
    background: var(--orange);
  }
  .line { position: absolute; line-height: 1; white-space: nowrap; }
  .attorney-name {
    right: 730px; text-align: right;
    color: var(--name-white);
    font-size: 35px; font-weight: 500; letter-spacing: 1.5px;
  }
  .attorney-title {
    right: 732px; top: 349px;
    color: var(--name-white);
    font-size: 21px; font-weight: 400; letter-spacing: 2px;
  }
  .firm-name {
    left: 496px; top: 90px;
    color: var(--green);
    font-size: 30px; font-weight: 500; letter-spacing: 1px;
  }
  .office-label {
    left: 496px;
    color: var(--orange);
    font-size: 25px; font-weight: 700; letter-spacing: 1px;
  }
  .detail {
    left: 496px;
    color: var(--green);
    font-size: 22px; font-weight: 400; letter-spacing: 1.3px;
  }
  .detail .small-caps { font-variant: small-caps; }
  .detail .tag { color: var(--orange); font-weight: 700; }
  .detail .gap { display: inline-block; width: 22px; }
</style>
</head>
<body>
  <article class="business-card">
    <div class="name-panel"></div>
    <div class="accent-band"></div>

    <p class="line attorney-name" style="top:252px;">DANIEL</p>
    <p class="line attorney-name" style="top:295px;">R. WHITAKER, SR.</p>
    <p class="line attorney-title">ATTORNEY AT LAW</p>

    <h1 class="line firm-name">THE WHITAKER LAW FIRM, P.C.</h1>

    <h2 class="line office-label" style="top:180px;">HOUSTON</h2>
    <p class="line detail" style="top:220px;">4410 KATY FREEWAY, SUITE 208</p>
    <p class="line detail" style="top:259px;">HOUSTON, TEXAS 77055</p>

    <h2 class="line office-label" style="top:343px;">WEST TEXAS</h2>
    <p class="line detail" style="top:384px;"><span class="small-caps">P.O. Box 518, Marathon, Texas</span> 79617</p>

    <p class="line detail" style="top:472px;"><span class="tag">P:</span> (713) 555-0142<span class="gap"></span><span class="tag">F:</span> (832) 555-0187</p>
    <p class="line detail" style="top:511px;"><span class="tag">E:</span> DANIEL@WHITAKERLEGAL.COM</p>
  </article>
</body>
</html>
```